IT Network Consultancy - Business Card

t4 linkways is a IT network consultancy based in London. We're looking for a smart, modern and professional business card design. Our website is here: www.t4linkways.co.uk

Key things that should be included on the card (with examples):

Company Logo
Name
Position / Job Title: Network Consultant
Mobile Phone Number: +44 (0) 7700 900418
Land Line: +44 (0) 1632 960274
Email Address: name@t4linkways.co.uk
Web Site URL: www.t4linkways.co.uk

Target Market(s)

Large enterprise / global companies / corporates

Industry/Entity Type

Business

Requirements
Must have
• Incorporate our logo - which is attached to the project. They are in AI format (can be opened in Inkscape).

The design should be double sided and fit on a UK standard 85mm × 55mm card and be in a format that retains the quality when printed.
Nice to have
• The project does not have to conform to the colour of our website but this should give you inspiration of the style we like.
Should not have
• Bright colours. Pictures are not necessary.

```html
<!DOCTYPE html>
<html lang="en">
<head>
<meta charset="utf-8">
<title>t4 linkways – Business Card</title>
<link rel="stylesheet" href="https://fonts.googleapis.com/css2?family=Quicksand:wght@300;400&display=swap">
<style>
  :root {
    --canvas-bg: #e6e3de;
    --card-dark: #17181c;
    --card-mid: #2b2d33;
    --card-light: #474a52;
    --stripe-light: #8a8e97;
    --stripe-mid: #4d5058;
    --text-light: #d9dce2;
    --text-soft: #a9adb6;
    --text-muted: #8d919a;
  }
  * { margin: 0; padding: 0; box-sizing: border-box; }
  html, body {
    width: 1200px;
    height: 900px;
    overflow: hidden;
    background: var(--canvas-bg);
    font-family: "Quicksand", sans-serif;
    font-weight: 300;
  }
  .canvas {
    position: relative;
    width: 1200px;
    height: 900px;
  }
  .card {
    position: absolute;
    left: 322px;
    width: 556px;
    height: 362px;
    overflow: hidden;
    background:
      radial-gradient(ellipse 70% 90% at 60% 45%, rgba(110,115,125,0.28), rgba(0,0,0,0) 70%),
      linear-gradient(160deg, var(--card-dark) 0%, var(--card-mid) 55%, var(--card-light) 100%);
    color: var(--text-light);
  }
  .card--front { top: 78px; }
  .card--back  { top: 458px; }

  .wordmark {
    font-family: "Quicksand", sans-serif;
    font-weight: 300;
    color: var(--text-light);
    letter-spacing: 0.06em;
    white-space: nowrap;
    display: flex;
    align-items: center;
  }
  .wordmark__square {
    display: inline-block;
    background: var(--text-light);
  }

  /* Front side */
  .card--front .wordmark {
    position: absolute;
    left: 0; right: 0;
    top: 148px;
    justify-content: center;
    font-size: 40px;
    gap: 16px;
  }
  .card--front .wordmark__square { width: 30px; height: 30px; }
  .front-stripes {
    position: absolute;
    left: 0; right: 0; bottom: 0;
    height: 36px;
  }
  .front-stripes__line {
    position: absolute;
    left: 0; right: 0; top: 0;
    height: 3px;
    background: linear-gradient(90deg, var(--stripe-mid), var(--stripe-light) 50%, var(--stripe-mid));
  }
  .front-stripes__band {
    position: absolute;
    left: 0; right: 0; top: 8px; bottom: 0;
    background: linear-gradient(180deg, var(--stripe-mid), #3a3d44);
  }

  /* Back side */
  .back-header {
    position: absolute;
    left: 0; right: 0; top: 0;
    height: 84px;
    background: linear-gradient(180deg, #1a1b1f, #24262b);
  }
  .card--back .wordmark {
    position: absolute;
    left: 28px;
    top: 22px;
    font-size: 26px;
    gap: 10px;
  }
  .card--back .wordmark__square { width: 20px; height: 20px; }
  .back-divider {
    position: absolute;
    left: 0; right: 0; top: 84px;
    height: 6px;
    background: linear-gradient(90deg, var(--stripe-mid), var(--stripe-light) 50%, var(--stripe-mid));
  }
  .person {
    position: absolute;
    left: 0; right: 0;
    top: 128px;
    text-align: center;
  }
  .person__name {
    font-size: 36px;
    font-weight: 300;
    color: var(--text-light);
    letter-spacing: 0.01em;
  }
  .person__role {
    margin-top: 8px;
    font-size: 19px;
    color: var(--text-soft);
    letter-spacing: 0.02em;
  }
  .contact {
    position: absolute;
    bottom: 22px;
    font-size: 14px;
    line-height: 20px;
    color: var(--text-muted);
    font-weight: 400;
  }
  .contact--phones { left: 24px; }
  .contact--online { right: 24px; text-align: right; }
</style>
</head>
<body>
<main class="canvas">

  <section class="card card--front" aria-label="Business card front">
    <div class="wordmark"><span class="wordmark__square"></span>T4 LINKWAYS</div>
    <div class="front-stripes">
      <div class="front-stripes__line"></div>
      <div class="front-stripes__band"></div>
    </div>
  </section>

  <section class="card card--back" aria-label="Business card back">
    <div class="back-header"></div>
    <div class="wordmark"><span class="wordmark__square"></span>T4 LINKWAYS</div>
    <div class="back-divider"></div>

    <div class="person">
      <p class="person__name">John Doe</p>
      <p class="person__role">network consultant</p>
    </div>

    <div class="contact contact--phones">
      <p>Mobile: +44 (0) 7700 900418</p>
      <p>Land Line: +44 (0) 1632 960274</p>
    </div>
    <div class="contact contact--online">
      <p>E-mail: name@t4linkways.co.uk</p>
      <p>Web: www.t4linkways.co.uk</p>
    </div>
  </section>

</main>
</body>
</html>
```